Fun Location App for users to earn rewards and vouchers everywhere they go

Tovrim is a social app where users can collect rewards when they travel + complete quests at different location to get rewards.

We would like a design of an app that has these features/function
1) Login/Signup Page
2) HomePage - A Map with your current location
- Show the location/stores aroudn
- Have a bag tab to press and get rewards
3) Quests Tab = show all the available tasks
4) Exchange Tab = all the items available for exchange vouchers and can click to know more
5) Wallet Tab = user profile + vouchers in their wallet
6) Partners Tab = Showcase all the partners and can click to know more
7) Claim functions

We have attached a visual example. Do feel free to change what is best fit too. We do need to exact measurements as well to create the app

Target Market(s)

Fun, people who like rewards and interact with friends

Font styles to use
Sans Serif

Colors
f78f20
fbed22
fbee3e

Requirements
Must have
• Yellow, fun interactive feeling.
Nice to have
• Pop up when click on things
Should not have
• nil

```html
<!DOCTYPE html>
<html lang="en">
<head>
<meta charset="utf-8">
<title>Tovrim – App Screens</title>
<link rel="stylesheet" href="https://fonts.googleapis.com/css2?family=Poppins:wght@400;500;600;700&family=Roboto:wght@400;500;700&display=swap">
<style>
  :root{
    --bg:#e49b1f;
    --orange:#f78f20;
    --amber:#f9a90f;
    --yellow:#fbed22;
    --yellow-soft:#fbee3e;
    --ink:#1c1c1e;
    --ink-2:#26262a;
    --navy:#33364f;
    --line:#3a3a3e;
    --white:#ffffff;
    --muted:#cfcfcf;
  }
  *{box-sizing:border-box;margin:0;padding:0}
  html,body{width:1015px;height:1200px;overflow:hidden}
  body{background:var(--bg);font-family:"Poppins",sans-serif;color:var(--white);position:relative}
  .icon-defs{position:absolute;width:0;height:0}

  .screen{position:absolute;width:232px;height:508px;border-radius:24px;overflow:hidden;background:var(--ink)}
  .screen--login{left:81px;top:62px}
  .screen--signup{left:390px;top:62px}
  .screen--map{left:699px;top:62px}
  .screen--wallet{left:81px;top:630px}
  .screen--quests{left:390px;top:630px}
  .screen--trade{left:699px;top:630px}
  .abs{position:absolute}

  /* brand */
  .brand{position:absolute;left:0;right:0;display:flex;flex-direction:column;align-items:center;gap:6px}
  .brand__dot{width:30px;height:30px;border-radius:50%;background:var(--yellow)}
  .brand__name{font-weight:700;font-size:28px;line-height:1;color:var(--white)}

  /* login */
  .screen--login{background:radial-gradient(circle at 50% 40%,#2c2c2f 0%,#161617 70%,#0f0f10 100%)}
  .login__title{position:absolute;top:194px;width:100%;text-align:center;font-weight:600;font-size:20px}
  .pill{position:absolute;left:17px;width:197px;height:35px;border-radius:18px;background:var(--white);color:#444;font-family:"Roboto",sans-serif;font-size:11px;padding-left:17px;display:flex;align-items:center}
  .login__forgot{position:absolute;top:336px;width:100%;text-align:center;font-family:"Roboto",sans-serif;font-size:10.5px;color:#e8e8e8}
  .btn-cta{position:absolute;left:17px;width:197px;height:36px;background:linear-gradient(180deg,var(--yellow-soft) 0%,var(--amber) 55%,var(--orange) 100%);display:flex;align-items:center;justify-content:center;font-family:"Roboto",sans-serif;font-weight:700;font-size:13px;letter-spacing:.5px;color:var(--white)}
  .btn-cta--round{border-radius:18px}

  /* signup */
  .signup__photo{position:absolute;inset:0;background:linear-gradient(160deg,#4a4747 0%,#2d2b2b 45%,#1d1c1c 100%)}
  .signup__subtitle{position:absolute;top:104px;width:100%;text-align:center;font-weight:600;font-size:14px}
  .field{position:absolute;left:17px;width:197px;height:36px;background:var(--white);color:#444;font-family:"Roboto",sans-serif;font-size:10.5px;padding-left:17px;display:flex;align-items:center;justify-content:space-between;padding-right:12px}

  /* map */
  .map__area{position:absolute;inset:0;background:var(--navy)}
  .map__pin{position:absolute;width:18px;height:22px}
  .map__venue{position:absolute;left:106px;top:215px;width:41px;height:41px;background:var(--white);border:2px solid var(--yellow);border-radius:3px}
  .map__me{position:absolute;left:113px;top:283px;width:16px;height:16px;border-radius:50%;background:#f5c37a;border:3px solid #b88a2d}
  .bag{position:absolute;left:19px;top:22px;width:193px;height:79px;background:var(--amber);border-radius:4px;padding:7px 5px 0}
  .bag__btn{height:22px;border-radius:4px;background:var(--ink);display:flex;align-items:center;justify-content:center;font-family:"Roboto",sans-serif;font-weight:500;font-size:10px;margin-bottom:4px}
  .bag__stats{display:flex;justify-content:center;gap:10px;font-family:"Roboto",sans-serif;font-weight:500;font-size:8.5px;color:var(--ink);margin-top:6px}

  /* bottom nav */
  .nav{position:absolute;left:0;right:0;bottom:0;height:28px;background:var(--white);display:flex;align-items:center;justify-content:space-around;padding:0 10px}
  .nav__icon{width:15px;height:15px;color:#f0b24a}
  .nav__home{width:38px;height:38px;border-radius:50%;background:var(--amber);display:flex;align-items:center;justify-content:center;margin-top:-12px}
  .nav__home svg{width:18px;height:22px;color:var(--white)}

  /* headers */
  .head{position:absolute;left:0;right:0;top:0;background:var(--amber)}
  .head__brand{position:absolute;right:12px;font-weight:700;font-size:13px;color:var(--white);display:flex;align-items:center;gap:4px}
  .head__brand i{width:9px;height:9px;border-radius:50%;background:var(--white);display:block}
  .head__title{position:absolute;left:13px;font-weight:600;color:var(--white);line-height:1.15}

  /* lists */
  .list{position:absolute;left:11px;right:11px}
  .row{display:flex;align-items:center;border-bottom:1px solid var(--line);position:relative}
  .thumb{width:51px;height:41px;flex:none;background:linear-gradient(180deg,#3a8fb0 0%,#2f5569 45%,#6b4a32 100%)}
  .thumb--food{width:52px;height:43px;background:linear-gradient(135deg,#e9e9e9 0%,#b48a6a 45%,#5a2f22 75%,#2d1b14 100%)}
  .row__text{margin-left:12px;flex:1}
  .row__name{font-weight:600;font-size:11px;line-height:1.2}
  .row__deal{font-family:"Roboto",sans-serif;font-size:9px;color:#eee;margin-top:3px}
  .chip{height:16px;border-radius:2px;background:var(--amber);color:var(--white);font-family:"Roboto",sans-serif;font-weight:500;font-size:7px;display:flex;align-items:center;justify-content:center}
  .chip--claim{width:47px}
  .chip--challenge{width:53px}
  .chip--get{width:40px;font-size:7.5px}
  .progress{width:95px;height:2px;background:var(--white);margin-top:3px;position:relative}
  .progress::before{content:"";position:absolute;left:0;top:0;height:2px;width:40%;background:var(--amber)}
  .row__cost{font-family:"Roboto",sans-serif;font-size:5.5px;font-weight:700;margin-top:2px}

  /* wallet */
  .screen--wallet,.screen--quests,.screen--trade{background:linear-gradient(180deg,#1e1e20 0%,#232325 60%,#1a1a1b 100%)}
  .avatar{position:absolute;left:14px;top:18px;width:42px;height:42px;border-radius:50%;background:linear-gradient(160deg,#d9a77f 0%,#a7724b 100%);border:2px solid #fff3}
  .profile__name{position:absolute;left:69px;top:15px;font-weight:600;font-size:15px;line-height:1}
  .profile__coins{position:absolute;left:69px;top:35px;font-weight:600;font-size:8.5px}
  .profile__ref{position:absolute;left:69px;top:49px;font-family:"Roboto",sans-serif;font-size:7px}
  .profile__ref b{font-weight:700;font-size:8px}
  .account{position:absolute;left:14px;right:14px;top:86px;font-family:"Roboto",sans-serif;font-size:8.5px;line-height:16px}
  .account__line{display:flex;justify-content:space-between}
  .account__label{font-weight:700}
  .account__hint{font-size:7.5px}
  .tabs{position:absolute;left:11px;right:11px;top:146px;height:23px;display:flex;gap:3px}
  .tab{flex:1;display:flex;align-items:center;justify-content:center;font-family:"Roboto",sans-serif;font-weight:500;font-size:8.5px}
  .tab--active{background:var(--amber);color:var(--white)}
  .tab--idle{background:var(--white);color:var(--ink)}
  .wallet__note{position:absolute;top:437px;width:100%;text-align:center;font-family:"Roboto",sans-serif;font-weight:500;font-size:8.5px;line-height:12.5px}
</style>
</head>
<body>

<svg class="icon-defs" aria-hidden="true">
  <defs>
    <symbol id="i-pin" viewBox="0 0 20 24"><path d="M10 1a8 8 0 0 0-8 8c0 6 8 14 8 14s8-8 8-14a8 8 0 0 0-8-8z" fill="currentColor"/><circle cx="10" cy="9" r="3.6" fill="#fff"/></symbol>
    <symbol id="i-grid" viewBox="0 0 16 16" fill="none" stroke="currentColor" stroke-width="1.4"><rect x="1" y="1" width="5.5" height="5.5"/><rect x="9.5" y="1" width="5.5" height="5.5"/><rect x="1" y="9.5" width="5.5" height="5.5"/><path d="M9.5 9.5h2.5v2.5M15 9.5v5.5h-5.5"/></symbol>
    <symbol id="i-user" viewBox="0 0 16 16" fill="none" stroke="currentColor" stroke-width="1.3"><circle cx="8" cy="8" r="7"/><circle cx="8" cy="6.3" r="2.5"/><path d="M3.6 12.8c1-1.9 2.6-2.8 4.4-2.8s3.4.9 4.4 2.8"/></symbol>
    <symbol id="i-chevron" viewBox="0 0 12 8" fill="none" stroke="currentColor" stroke-width="1.6"><path d="M1.5 1.5L6 6l4.5-4.5"/></symbol>
  </defs>
</svg>

<!-- Login -->
<section class="screen screen--login" role="img" aria-label="Login screen on a dark background with faint network lines">
  <div class="brand" style="top:68px"><span class="brand__dot"></span><span class="brand__name">Tovrim</span></div>
  <h1 class="login__title">LOGIN</h1>
  <div class="pill" style="top:234px">Username</div>
  <div class="pill" style="top:284px">Password</div>
  <p class="login__forgot">Forgot your password?</p>
  <div class="btn-cta btn-cta--round" style="top:367px">LOGIN</div>
</section>

<!-- Signup -->
<section class="screen screen--signup">
  <div class="signup__photo" role="img" aria-label="Dim photo of a person wearing glasses looking at a phone"></div>
  <div class="brand" style="top:22px"><span class="brand__dot"></span><span class="brand__name">Tovrim</span></div>
  <h2 class="signup__subtitle">New user signup</h2>
  <div class="field" style="top:138px">First Name:*</div>
  <div class="field" style="top:182px">Last Name*:</div>
  <div class="field" style="top:226px">Username*:</div>
  <div class="field" style="top:270px">Date of birth*:</div>
  <div class="field" style="top:313px">Email*:</div>
  <div class="field" style="top:357px">Referral Code / Account Code:</div>
  <div class="field" style="top:401px">Gender*: <svg width="9" height="6"><use href="#i-chevron"/></svg></div>
  <div class="btn-cta" style="top:444px">NEXT</div>
</section>

<!-- Map home -->
<section class="screen screen--map">
  <div class="map__area" role="img" aria-label="Dark street map of the area around the user with building outlines"></div>
  <svg class="map__pin" style="left:80px;top:188px;color:var(--yellow)"><use href="#i-pin"/></svg>
  <svg class="map__pin" style="left:165px;top:186px;color:var(--yellow)"><use href="#i-pin"/></svg>
  <svg class="map__pin" style="left:178px;top:333px;color:var(--yellow)"><use href="#i-pin"/></svg>
  <svg class="map__pin" style="left:41px;top:388px;color:var(--yellow)"><use href="#i-pin"/></svg>
  <div class="map__venue" role="img" aria-label="Partner venue badge"></div>
  <div class="map__me" aria-label="Your location"></div>
  <div class="bag">
    <div class="bag__btn">ADS/MESSAGE</div>
    <div class="bag__btn">OPEN YOUR BAG</div>
    <div class="bag__stats"><span>5000 x tovcoins</span><span>|</span><span>5 x voucher</span></div>
  </div>
  <nav class="nav">
    <svg class="nav__icon"><use href="#i-grid"/></svg>
    <svg class="nav__icon"><use href="#i-user"/></svg>
    <span class="nav__home"><svg><use href="#i-pin"/></svg></span>
    <svg class="nav__icon"><use href="#i-grid"/></svg>
    <svg class="nav__icon"><use href="#i-user"/></svg>
  </nav>
</section>

<!-- Wallet / profile -->
<section class="screen screen--wallet">
  <header class="head" style="height:70px">
    <div class="avatar" role="img" aria-label="Profile photo"></div>
    <div class="profile__name">Nickname</div>
    <div class="profile__coins">55,000 tovcoins</div>
    <div class="profile__ref">Referral code <b>ebK3Q</b></div>
    <div class="head__brand" style="top:28px"><i></i>Tovrim</div>
  </header>
  <div class="account">
    <div class="account__line"><span class="account__label">Account</span><span class="account__hint">(tap to change)</span></div>
    <div class="account__line"><span>+65 5550-0142</span><span style="margin-right:44px">@nickname</span></div>
    <div>nickname@tovmail.com</div>
  </div>
  <div class="tabs"><span class="tab tab--active">Vouchers</span><span class="tab tab--idle">Swarm</span></div>
  <div class="list" style="top:172px">
    <div class="row" style="height:62px"><div class="thumb" role="img" aria-label="Restaurant interior"></div><div class="row__text"><div class="row__name">Cobble Row</div><div class="row__deal">$1 off for any item</div></div><span class="chip chip--claim">Claim</span></div>
    <div class="row" style="height:62px"><div class="thumb" role="img" aria-label="Restaurant interior"></div><div class="row__text"><div class="row__name">Cobble Row</div><div class="row__deal">$1 off for any item</div></div><span class="chip chip--claim">Claim</span></div>
    <div class="row" style="height:62px"><div class="thumb" role="img" aria-label="Restaurant interior"></div><div class="row__text"><div class="row__name">Cobble Row</div><div class="row__deal">$1 off for any item</div></div><span class="chip chip--claim">Claim</span></div>
    <div class="row" style="height:62px"><div class="thumb" role="img" aria-label="Restaurant interior"></div><div class="row__text"><div class="row__name">Cobble Row</div><div class="row__deal">$1 off for any item</div></div><span class="chip chip--claim">Claim</span></div>
  </div>
  <p class="wallet__note">Travel and challenge our quests<br>to earn more vouchers</p>
  <nav class="nav">
    <svg class="nav__icon"><use href="#i-grid"/></svg>
    <svg class="nav__icon"><use href="#i-user"/></svg>
    <span class="nav__home"><svg><use href="#i-pin"/></svg></span>
    <svg class="nav__icon"><use href="#i-grid"/></svg>
    <svg class="nav__icon"><use href="#i-user"/></svg>
  </nav>
</section>

<!-- Quests -->
<section class="screen screen--quests">
  <header class="head" style="height:56px">
    <div class="head__title" style="top:12px;font-size:13px">Quest Time!<br><span style="font-size:11px">Challenge to earn rewards</span></div>
    <div class="head__brand" style="top:20px"><i></i>Tovrim</div>
  </header>
  <div class="list" style="top:69px">
    <div class="row" style="height:63px"><div class="thumb" role="img" aria-label="Restaurant interior"></div><div class="row__text"><div class="row__name">Cobble Row</div><div class="row__deal">$1 off for any item</div></div><span class="chip chip--challenge">Challenge</span></div>
    <div class="row" style="height:63px"><div class="thumb" role="img" aria-label="Restaurant interior"></div><div class="row__text"><div class="row__name">Cobble Row</div><div class="row__deal">$1 off for any item</div></div><span class="chip chip--challenge">Challenge</span></div>
    <div class="row" style="height:63px"><div class="thumb" role="img" aria-label="Restaurant interior"></div><div class="row__text"><div class="row__name">Cobble Row</div><div class="row__deal">$1 off for any item</div></div><span class="chip chip--challenge">Challenge</span></div>
    <div class="row" style="height:63px"><div class="thumb" role="img" aria-label="Restaurant interior"></div><div class="row__text"><div class="row__name">Cobble Row</div><div class="row__deal">$1 off for any item</div></div><span class="chip chip--challenge">Challenge</span></div>
    <div class="row" style="height:66px"><div class="thumb" role="img" aria-label="Restaurant interior"></div><div class="row__text"><div class="row__name">Cobble Row</div><div class="row__deal">$1 off for any item</div></div><span class="chip chip--challenge">Challenge</span></div>
    <div class="row" style="height:63px"><div class="thumb" role="img" aria-label="Restaurant interior"></div><div class="row__text"><div class="row__name">Cobble Row</div><div class="row__deal">$1 off for any item</div></div><span class="chip chip--challenge">Challenge</span></div>
  </div>
  <nav class="nav" style="height:31px">
    <svg class="nav__icon"><use href="#i-grid"/></svg>
    <svg class="nav__icon"><use href="#i-user"/></svg>
    <span class="nav__home"><svg><use href="#i-pin"/></svg></span>
    <svg class="nav__icon"><use href="#i-grid"/></svg>
    <svg class="nav__icon"><use href="#i-user"/></svg>
  </nav>
</section>

<!-- Trade -->
<section class="screen screen--trade">
  <header class="head" style="height:56px">
    <div class="head__title" style="top:12px;font-size:14px">Trade<br><span style="font-size:11px">55,000 tovcoins</span></div>
    <div class="head__brand" style="top:20px"><i></i>Tovrim</div>
  </header>
  <div class="list" style="left:8px;right:11px;top:63px">
    <div class="row" style="height:67px"><div class="thumb thumb--food" role="img" aria-label="Plated steak dish"></div><div class="row__text" style="margin-left:9px"><div class="row__name">Cobble Row</div><div class="row__deal">$0.50 off any food item</div><div class="row__cost">4000 tovcoins</div><div class="progress"></div></div><span class="chip chip--get">Get it</span></div>
    <div class="row" style="height:65px"><div class="thumb thumb--food" role="img" aria-label="Plated steak dish"></div><div class="row__text" style="margin-left:9px"><div class="row__name">Cobble Row</div><div class="row__deal">$0.50 off any food item</div><div class="row__cost">4000 tovcoins</div><div class="progress"></div></div><span class="chip chip--get">Get it</span></div>
    <div class="row" style="height:66px"><div class="thumb thumb--food" role="img" aria-label="Plated steak dish"></div><div class="row__text" style="margin-left:9px"><div class="row__name">Cobble Row</div><div class="row__deal">$0.50 off any food item</div><div class="row__cost">4000 tovcoins</div><div class="progress"></div></div><span class="chip chip--get">Get it</span></div>
    <div class="row" style="height:66px"><div class="thumb thumb--food" role="img" aria-label="Plated steak dish"></div><div class="row__text" style="margin-left:9px"><div class="row__name">Cobble Row</div><div class="row__deal">$0.50 off any food item</div><div class="row__cost">4000 tovcoins</div><div class="progress"></div></div><span class="chip chip--get">Get it</span></div>
    <div class="row" style="height:65px"><div class="thumb thumb--food" role="img" aria-label="Plated steak dish"></div><div class="row__text" style="margin-left:9px"><div class="row__name">Cobble Row</div><div class="row__deal">$0.50 off any food item</div><div class="row__cost">4000 tovcoins</div><div class="progress"></div></div><span class="chip chip--get">Get it</span></div>
    <div class="row" style="height:66px"><div class="thumb thumb--food" role="img" aria-label="Plated steak dish"></div><div class="row__text" style="margin-left:9px"><div class="row__name">Cobble Row</div><div class="row__deal">$0.50 off any food item</div><div class="row__cost">4000 tovcoins</div><div class="progress"></div></div><span class="chip chip--get">Get it</span></div>
  </div>
  <nav class="nav" style="height:31px">
    <svg class="nav__icon"><use href="#i-grid"/></svg>
    <svg class="nav__icon"><use href="#i-user"/></svg>
    <span class="nav__home"><svg><use href="#i-pin"/></svg></span>
    <svg class="nav__icon"><use href="#i-grid"/></svg>
    <svg class="nav__icon"><use href="#i-user"/></svg>
  </nav>
</section>

</body>
</html>
```